Home Security Company Business Card

Looking for a eye catching business card that is non traditional and stands out but yet still looks professional. It should include all the pertinent information such as name, title, address, telephone, e-mail, website address should definitely stand out and then finally the logo.

Target Market(s)

Residential and Commercial accounts mostly upscale accounts

Industry/Entity Type

Security

Contact Information for Business Card

Name
Title
Address
Office #
Cell #
E-mail
Website

Font styles to use
Serif
Sans Serif

Requirements
Must have
• Logo, two sided color configuration
Nice to have
• You decide
Should not have
• There really aren't any.

```html
<!DOCTYPE html>
<html lang="en">
<head>
<meta charset="utf-8">
<title>Halverton Home Protection — Business Card</title>
<link rel="stylesheet" href="https://fonts.googleapis.com/css2?family=Arimo:wght@400&family=Tinos:wght@400&display=swap">
<style>
  :root {
    --stage: #3b3431;
    --card: #1d1d1e;
    --ink: #f2f2f2;
    --brand-red: #a3221a;
    --brand-gold: #d9a12a;
    --icon-red: #b3261c;
  }
  * { margin: 0; padding: 0; box-sizing: border-box; }
  html, body { width: 1200px; height: 787px; overflow: hidden; }
  body {
    background: var(--stage);
    font-family: "Arimo", Arial, sans-serif;
    color: var(--ink);
    position: relative;
  }
  .card {
    position: absolute;
    top: 239px;
    width: 540px;
    height: 309px;
    background: var(--card);
    box-shadow: 0 10px 28px rgba(0,0,0,0.45);
  }
  .card-back { left: 50px; }
  .card-front { left: 610px; }

  .brand {
    display: flex;
    align-items: center;
    gap: 12px;
  }
  .brand-mark {
    width: 40px; height: 40px;
    border-radius: 50%;
    background: var(--brand-gold);
    flex: none;
  }
  .brand-name {
    font-family: "Tinos", "Times New Roman", serif;
    color: var(--brand-red);
    font-size: 22px;
    letter-spacing: 0.5px;
    line-height: 1.1;
    text-transform: uppercase;
  }

  /* back side */
  .card-back .brand {
    position: absolute;
    left: 0; right: 0; top: 110px;
    justify-content: center;
  }
  .card-back .brand-mark { width: 54px; height: 54px; }
  .card-back .brand-name { font-size: 26px; }
  .back-website {
    position: absolute;
    left: 0; right: 0; bottom: 58px;
    text-align: center;
    font-size: 14px;
    letter-spacing: 4px;
  }

  /* front side */
  .card-front .brand {
    position: absolute;
    left: 34px; top: 38px;
  }
  .address {
    position: absolute;
    left: 86px; top: 108px;
    font-size: 15px;
    line-height: 21px;
  }
  .contact-list {
    position: absolute;
    left: 60px; top: 160px;
    list-style: none;
    font-size: 15px;
  }
  .contact-list li {
    display: flex;
    align-items: center;
    gap: 12px;
    height: 22px;
  }
  .contact-icon { width: 14px; height: 14px; fill: var(--icon-red); flex: none; }
  .person {
    position: absolute;
    right: 46px; bottom: 40px;
    text-align: center;
  }
  .person-name { color: var(--brand-red); font-size: 19px; line-height: 24px; }
  .person-title { color: var(--brand-gold); font-size: 17px; line-height: 22px; }
</style>
</head>
<body>

<section class="card card-back" aria-label="Card back">
  <div class="brand">
    <span class="brand-mark"></span>
    <span class="brand-name">Halverton Home Protection</span>
  </div>
  <p class="back-website">www.halvertonhome.com</p>
</section>

<section class="card card-front" aria-label="Card front">
  <div class="brand">
    <span class="brand-mark"></span>
    <span class="brand-name">Halverton Home Protection</span>
  </div>

  <address class="address" style="font-style:normal">
    2710 Ashcombe Lane<br>
    Brookvale, NY 11920
  </address>

  <ul class="contact-list">
    <li>
      <svg class="contact-icon" viewBox="0 0 16 16" aria-hidden="true"><path d="M1 5c0-2 2-3 7-3s7 1 7 3v1h-4V4.5H5V6H1zM3 7h10l1 7H2zm5 1.5a2.2 2.2 0 1 0 0 4.4 2.2 2.2 0 0 0 0-4.4z"/></svg>
      <span>555 0148 2290</span>
    </li>
    <li>
      <svg class="contact-icon" viewBox="0 0 16 16" aria-hidden="true"><path d="M4 0h8a1 1 0 0 1 1 1v14a1 1 0 0 1-1 1H4a1 1 0 0 1-1-1V1a1 1 0 0 1 1-1zm1 2v10h6V2zm3 11a1 1 0 1 0 0 2 1 1 0 0 0 0-2z"/></svg>
      <span>555 0193 6471</span>
    </li>
    <li>
      <svg class="contact-icon" viewBox="0 0 16 16" aria-hidden="true"><path d="M0 3h16v1L8 9 0 4zm0 2.5 8 5 8-5V13H0z"/></svg>
      <span>marcus@halvertonhome.com</span>
    </li>
    <li>
      <svg class="contact-icon" viewBox="0 0 16 16" aria-hidden="true"><path d="M8 0a8 8 0 1 0 0 16A8 8 0 0 0 8 0zm0 2.5a2 2 0 1 1 0 4 2 2 0 0 1 0-4zM4.5 12c0-2.3 1.6-4 3.5-4s3.5 1.7 3.5 4z"/></svg>
      <span>www.halvertonhome.com</span>
    </li>
  </ul>

  <div class="person">
    <p class="person-name">Marcus Hale</p>
    <p class="person-title">President</p>
  </div>
</section>

</body>
</html>
```